Brightwell Auto Care 4x9 Rack Card

Design a 4" wide by 9" tall rack card printed front and back using the copy, logo and images uploaded below. I am also uploading a current flyer so you can see the typestyles we use. I will get the exact name of the font for you ASAP. Also will be uploading some before and after pictures for the back of the rack card

Target Market(s)

Affluent consumers who need their car cleaned and detailed in a meticulous fashion

Requirements
Must have
• Under the logo, put the words...... Premium Steam Detailing & Ceramic Coating.........also put ther following wording on the front side: Get Steamed! We use steam to clean your vehicle helping save millions of gallons of water and protecting our rivers, streams and lakes from runoff.
Nice to have
• a screened back background of hexagons might be nice

```html
<!DOCTYPE html>
<html lang="en">
<head>
<meta charset="utf-8">
<title>Brightwell Auto Care Rack Card</title>
<link href="https://fonts.googleapis.com/css2?family=Montserrat:wght@300;400;500;600;700&display=swap" rel="stylesheet">
<style>
:root{
  --bg:#d4d4d4;
  --paper:#ffffff;
  --blue:#4a80c4;
  --green:#6fac4c;
  --ink:#1d1d1d;
  --photo-warm:#8a6a45;
  --photo-dark:#2c2f33;
  --photo-grey:#6e7378;
  --photo-blue:#2a5fb8;
}
*{margin:0;padding:0;box-sizing:border-box}
html,body{width:1200px;height:2515px;overflow:hidden;background:var(--bg)}
body{position:relative;font-family:"Montserrat",sans-serif;color:var(--ink)}
.card{position:absolute;top:123px;width:486px;height:1093px;background:var(--paper);box-shadow:0 4px 10px rgba(0,0,0,.35);overflow:hidden}
.card-front{left:98px}
.card-back{left:616px}
.abs{position:absolute}

/* front */
.brand{left:38px;top:62px;display:flex;align-items:center;gap:14px}
.brand-dot{width:46px;height:46px;border-radius:50%;background:var(--blue)}
.brand-name{font-size:25px;font-weight:600;color:var(--green);line-height:1.05;letter-spacing:.5px}
.tagline{left:36px;top:153px;font-size:23px;font-weight:700;color:var(--green);line-height:22px;letter-spacing:-.5px}
.ribbon{left:0;top:215px;width:472px;height:46px;background:var(--blue);clip-path:polygon(0 0,460px 0,100% 50%,460px 100%,0 100%);color:#fff;font-size:24px;font-weight:700;letter-spacing:-.6px;line-height:46px;padding-left:36px;white-space:nowrap}
.hero-photo{left:10px;top:292px;width:476px;height:430px;background:radial-gradient(ellipse at 70% 40%,var(--photo-blue) 0%,var(--photo-warm) 45%,var(--photo-dark) 100%);clip-path:polygon(12% 0,88% 0,100% 30%,100% 70%,75% 100%,25% 100%,0 70%,0 30%)}
.steam-panel{left:0;top:745px;width:470px;height:168px;background:var(--blue);clip-path:polygon(0 0,430px 0,100% 50%,430px 100%,0 100%);color:#fff;padding:16px 0 0 37px}
.steam-title{font-size:29px;font-weight:700;letter-spacing:-.8px;line-height:34px}
.steam-copy{font-size:20px;font-weight:300;line-height:24px;letter-spacing:-.7px;white-space:nowrap}
.contact-band{left:38px;top:931px;width:448px;height:166px;background:var(--green);clip-path:polygon(40px 0,100% 0,100% 100%,40px 100%,0 50%);color:#fff}
.contact{position:absolute;font-size:12px;line-height:15px;letter-spacing:-.4px;font-weight:300;white-space:nowrap}
.contact b{font-weight:600;display:block}
.contact.sep{border-left:1px solid rgba(255,255,255,.6);padding-left:9px}
.icon{position:absolute;left:46px}

/* back */
.shot{position:absolute;height:147px}
.shot-before{left:0;width:265px;clip-path:polygon(0 0,88% 0,100% 50%,88% 100%,0 100%);background:linear-gradient(135deg,var(--photo-grey),var(--photo-dark))}
.shot-after{left:238px;width:248px;clip-path:polygon(12% 0,100% 0,100% 100%,12% 100%,0 50%);background:linear-gradient(135deg,#a9adb1,var(--photo-dark))}
.tag{position:absolute;height:45px;color:#fff;font-size:23px;font-weight:600;line-height:45px}
.tag-before{left:0;width:110px;background:var(--blue);clip-path:polygon(0 0,100% 0,90% 100%,0 100%);padding-left:17px}
.tag-after{right:0;width:108px;background:var(--green);clip-path:polygon(10% 0,100% 0,100% 100%,0 100%);padding-left:20px}
.menu-title{left:64px;top:764px;font-size:28px;font-weight:700;color:var(--green);letter-spacing:-.6px}
.menu-item{position:absolute;left:64px;font-size:18px;font-weight:400;letter-spacing:-.3px;line-height:18px;white-space:nowrap}
.price{position:absolute;left:347px;width:100px;height:29px;background:var(--blue);clip-path:polygon(6px 0,100% 0,100% 100%,6px 100%,0 50%);color:#fff;font-size:15px;font-weight:300;text-align:center;line-height:29px}
.cta{left:0;top:1042px;width:444px;height:47px;background:var(--green);clip-path:polygon(0 0,432px 0,100% 50%,432px 100%,0 100%);color:#fff;font-size:27px;font-weight:500;letter-spacing:-.6px;line-height:47px;padding-left:52px;white-space:nowrap}
.cta svg{position:absolute;left:52px;top:12px}
</style>
</head>
<body>

<section class="card card-front">
  <div class="abs brand"><span class="brand-dot"></span><span class="brand-name">BRIGHTWELL<br>AUTO CARE</span></div>
  <h2 class="abs tagline">Premium Steam Detailing<br>And Ceramic Coating</h2>
  <div class="abs ribbon">Fall In Love With Your Car Again!</div>
  <div class="abs hero-photo" role="img" aria-label="Hexagon photo collage of a detailer steam cleaning a luxury car"></div>
  <div class="abs steam-panel">
    <h3 class="steam-title">Get Steamed!</h3>
    <p class="steam-copy">We use steam to clean your vehicle<br>helping save millions of gallons of water<br>&amp; protecting our rivers, streams &amp; lakes<br>from runoff.</p>
  </div>
  <div class="abs contact-band">
    <svg class="icon" style="top:38px" width="11" height="11" viewBox="0 0 24 24"><path fill="#fff" d="M6.6 10.8a15 15 0 006.6 6.6l2.2-2.2c.3-.3.7-.4 1-.2 1.1.4 2.3.6 3.6.6.6 0 1 .4 1 1V20c0 .6-.4 1-1 1A17 17 0 013 4c0-.6.4-1 1-1h3.5c.6 0 1 .4 1 1 0 1.3.2 2.5.6 3.6.1.3 0 .7-.2 1z"/></svg>
    <div class="contact" style="left:62px;top:36px"><b>Aspen/Snowmass</b>(970) 555-0142</div>
    <div class="contact sep" style="left:206px;top:36px"><b>Vail</b>(970) 555-0187</div>
    <div class="contact sep" style="left:326px;top:36px"><b>Boulder</b>(720) 555-0163</div>
    <svg class="icon" style="top:94px" width="10" height="13" viewBox="0 0 24 30"><path fill="#fff" d="M12 0a11 11 0 00-11 11c0 8 11 19 11 19s11-11 11-19A11 11 0 0012 0zm0 15a4 4 0 110-8 4 4 0 010 8z"/></svg>
    <div class="contact" style="left:62px;top:92px"><b>Maple Court</b>Shops 1420 Pine<br>Street Boulder</div>
    <div class="contact sep" style="left:206px;top:92px"><b>96 Ridge Road</b>Suite 40 Avon</div>
    <div class="contact sep" style="left:326px;top:92px"><b>12 Aspen Loop</b>Snowmass Village</div>
  </div>
</section>

<section class="card card-back">
  <div class="shot shot-before" style="top:40px" role="img" aria-label="Dirty engine bay before cleaning"></div>
  <div class="shot shot-after" style="top:112px" role="img" aria-label="Clean engine bay after steam cleaning"></div>
  <div class="tag tag-before" style="top:166px">Before</div>
  <div class="tag tag-after" style="top:237px">After</div>

  <div class="shot shot-before" style="top:277px" role="img" aria-label="Soiled car interior floor before cleaning"></div>
  <div class="shot shot-after" style="top:350px" role="img" aria-label="Clean car interior after steam cleaning"></div>
  <div class="tag tag-before" style="top:401px">Before</div>
  <div class="tag tag-after" style="top:474px">After</div>

  <div class="shot shot-before" style="top:502px" role="img" aria-label="Greasy truck engine before cleaning"></div>
  <div class="shot shot-after" style="top:575px" role="img" aria-label="Clean truck engine after steam cleaning"></div>
  <div class="tag tag-before" style="top:624px">Before</div>
  <div class="tag tag-after" style="top:697px">After</div>

  <h3 class="abs menu-title">Ceramic Coating</h3>
  <p class="menu-item" style="top:814px">Premium Steam Washes</p>
  <p class="menu-item" style="top:852px">Full Steam Detailing</p>
  <p class="menu-item" style="top:883px">Paint Correction<br>(multi-stage polishing)</p>
  <p class="menu-item" style="top:931px">Headlight Restoration</p>
  <p class="menu-item" style="top:970px">Engine Steam Cleaning</p>
  <div class="price" style="top:808px">$100 &amp; up</div>
  <div class="price" style="top:847px">$275 &amp; up</div>
  <div class="price" style="top:886px">$650 &amp; up</div>
  <div class="price" style="top:926px">$110</div>
  <div class="price" style="top:965px">$75</div>
  <div class="abs cta">
    <svg width="14" height="24" viewBox="0 0 14 24"><path fill="none" stroke="#fff" stroke-width="3" stroke-linecap="round" d="M11 3C4 5 4 19 11 21"/></svg>
    <span style="padding-left:20px">Call or visit us for a quote</span>
  </div>
</section>

</body>
</html>
```